Social Media Application Design - Android and IOS

I am ready to go live with new social media app however I am not comfortable with the current design. It is a not interactive or attractive enough. Please note the splash screen is a green, so preference would be to keep a green theme although I am more than happy to consider other colours that would improve the design.
The attachment has the app screens that need to be redesigned. They may not need massive changes , however keen to go live so looking for inspired designers to support with this project and many others that I have, including ongoing work on this app.
Target Market(s)
Millenials
Industry/Entity Type
Social
Colors
Designer to choose colors to be used in the design.
Requirements
Must have
- Please see attached document for screens that I would like redesigned. It needs to work with Android and IOS. I am looking for the design and not the functionality.
Nice to have
- Highly interactive design. Please see polling functionality of Pictavo.
Should not have
- should not be complicated - simplicity is the key

```html
<!DOCTYPE html>
<html lang="en">
<head>
<meta charset="utf-8">
<title>Ask – Choose a Topic</title>
<link rel="stylesheet" href="https://fonts.googleapis.com/css2?family=Ubuntu:wght@400;500;700&display=swap">
<style>
  :root {
    --header-top: #6a35a8;
    --header-mid: #7d3cc0;
    --header-bottom: #5f25b0;
    --body-top: #8549cf;
    --body-bottom: #a34cd2;
    --chip-light: #9550d8;
    --chip-dark: #6f2edb;
    --search-field: #f7f6f6;
    --search-button: #8a45d2;
    --placeholder: #9a9a9a;
    --white: #ffffff;
  }
  * { box-sizing: border-box; margin: 0; padding: 0; }
  html, body { width: 675px; height: 1200px; overflow: hidden; }
  body {
    position: relative;
    font-family: "Ubuntu", sans-serif;
    background: linear-gradient(180deg, var(--body-top) 0%, var(--body-bottom) 100%);
    color: var(--white);
  }
  .hero {
    position: absolute; left: 0; top: 0; width: 675px; height: 387px;
    background:
      radial-gradient(ellipse at 60% 25%, rgba(170,110,220,.35), transparent 60%),
      linear-gradient(180deg, var(--header-top) 0%, var(--header-mid) 55%, var(--header-bottom) 100%);
  }
  .status-bar {
    position: absolute; left: 0; top: 0; width: 675px; height: 40px;
    display: flex; align-items: center; padding: 0 14px;
    font-family: "Helvetica Neue", Arial, sans-serif; font-size: 21px;
  }
  .signal { display: flex; gap: 3px; margin-right: 10px; }
  .signal span { width: 10px; height: 10px; border-radius: 50%; background: var(--white); }
  .signal span.empty { background: transparent; border: 1.5px solid var(--white); }
  .carrier { margin-right: 12px; }
  .status-right { margin-left: auto; display: flex; align-items: center; gap: 8px; }
  .battery { width: 42px; height: 18px; border: 1.5px solid var(--white); border-radius: 4px; padding: 2px; position: relative; }
  .battery::before { content: ""; display: block; width: 100%; height: 100%; background: var(--white); border-radius: 1.5px; }
  .battery::after { content: ""; position: absolute; right: -5px; top: 5px; width: 3px; height: 6px; background: var(--white); border-radius: 0 2px 2px 0; }
  .search {
    position: absolute; left: 87px; top: 131px; width: 503px; height: 73px;
    display: flex; border-radius: 6px; overflow: hidden;
  }
  .search-field {
    flex: 1; background: var(--search-field); color: var(--placeholder);
    font-family: "Helvetica Neue", Arial, sans-serif; font-size: 25px;
    display: flex; align-items: center; padding-left: 25px;
  }
  .search-button { width: 79px; background: var(--search-button); display: flex; align-items: center; justify-content: center; }
  .prompt {
    position: absolute; left: 0; top: 240px; width: 675px; text-align: center;
    font-weight: 700; font-size: 26px; letter-spacing: .3px;
  }
  .topic {
    position: absolute; width: 194px; height: 58px; border-radius: 3px;
    display: flex; align-items: center; justify-content: center;
    font-weight: 500; font-size: 15.5px; letter-spacing: .6px;
    box-shadow: 0 2px 4px rgba(60,10,120,.18);
  }
  .topic.fade-down { background: linear-gradient(180deg, var(--chip-light), var(--chip-dark)); }
  .topic.fade-up { background: linear-gradient(180deg, var(--chip-dark), var(--chip-light)); }
</style>
</head>
<body>
  <div class="hero" role="img" aria-label="Photo of a musician playing guitar under purple stage light"></div>

  <div class="status-bar">
    <div class="signal"><span></span><span></span><span></span><span></span><span class="empty"></span></div>
    <span class="carrier">Carrier</span>
    <svg width="22" height="16" viewBox="0 0 22 16"><path d="M1 5a15 15 0 0 1 20 0M4.5 8.5a10 10 0 0 1 13 0M8 12a5 5 0 0 1 6 0" fill="none" stroke="#fff" stroke-width="2.4" stroke-linecap="round"/><circle cx="11" cy="14.5" r="1.5" fill="#fff"/></svg>
    <div class="status-right">
      <svg width="20" height="20" viewBox="0 0 20 20"><circle cx="10" cy="10" r="8.5" fill="none" stroke="#fff" stroke-width="1.5"/><rect x="6.5" y="9" width="7" height="5.5" rx="1" fill="#fff"/><path d="M8 9V7.5a2 2 0 0 1 4 0V9" fill="none" stroke="#fff" stroke-width="1.4"/></svg>
      <span>100%</span>
      <div class="battery"></div>
    </div>
  </div>

  <div class="search">
    <div class="search-field">Search</div>
    <div class="search-button">
      <svg width="34" height="34" viewBox="0 0 34 34"><circle cx="14" cy="14" r="10" fill="none" stroke="#fff" stroke-width="4.5"/><path d="M21.5 21.5l8 8" stroke="#fff" stroke-width="5" stroke-linecap="round"/></svg>
    </div>
  </div>

  <h1 class="prompt">WHAT IS YOUR QUESTION ABOUT?</h1>

  <div class="topic fade-down" style="left:31px;top:467px">SCIENCE</div>
  <div class="topic fade-down" style="left:240px;top:467px">TECHNOLOGY</div>
  <div class="topic fade-down" style="left:450px;top:467px">GADGETS</div>
  <div class="topic fade-down" style="left:132px;top:545px">HEALTH</div>
  <div class="topic fade-down" style="left:339px;top:545px">FASHION</div>

  <div class="topic fade-up" style="left:31px;top:711px">HISTORY</div>
  <div class="topic fade-up" style="left:240px;top:711px">LANGUAGES</div>
  <div class="topic fade-up" style="left:450px;top:711px">EDUCATION</div>
  <div class="topic fade-up" style="left:132px;top:788px">BUSINESS</div>
  <div class="topic fade-up" style="left:339px;top:788px">FINANCE</div>

  <div class="topic fade-up" style="left:31px;top:938px">MY COUNTY</div>
  <div class="topic fade-up" style="left:240px;top:938px">MY CITY</div>
  <div class="topic fade-up" style="left:450px;top:938px">RELIGION</div>
  <div class="topic fade-up" style="left:132px;top:1015px">TRAVEL</div>
  <div class="topic fade-up" style="left:339px;top:1015px">BEAUTY</div>
</body>
</html>
```